Need Power Point Presentation - That incorporates New Logo

We have a new logo and would like to incorporate it into a Power Point template. We are looking for title page, 2 body pages and a closing page design. If you have any questions please let me know. New logo is attached.

```html
<!DOCTYPE html>
<html lang="en">
<head>
<meta charset="utf-8">
<title>Norvelle Presentation Template</title>
<link href="https://fonts.googleapis.com/css2?family=Roboto:wght@300;400;500;700&display=swap" rel="stylesheet">
<style>
:root{
  --sheet:#d3d6db;
  --paper:#f6f6f6;
  --white:#ffffff;
  --blue:#4fb0e4;
  --blue-deep:#3f95cc;
  --navy:#2e3544;
  --navy-line:#3d4556;
  --grey:#9a9ea6;
  --ink:#444a55;
  --rule:#e6e7ea;
  --pie-green:#a3d13b;
  --pie-pink:#e3566f;
  --pie-purple:#a845b0;
  --teal-soft:#a9dcee;
}
*{box-sizing:border-box;margin:0;padding:0}
html,body{width:1059px;height:1200px;overflow:hidden;background:var(--sheet);font-family:'Roboto',Arial,sans-serif}
.canvas{position:relative;width:1059px;height:1200px}
.slide{position:absolute;width:582px;height:436px;transform:scale(.8825);transform-origin:0 0;overflow:hidden;background:var(--paper)}
.col-a{left:12.4px}.col-b{left:533.9px}
.row-1{top:8.8px}.row-2{top:405px}.row-3{top:801.3px}

.brand{position:absolute;font-family:'Roboto',Arial,sans-serif;font-weight:400;letter-spacing:2px;white-space:nowrap}
.brand-blue{color:var(--blue)}
.brand-white{color:var(--white)}

/* title slide */
.title-slide{background:var(--blue)}
.title-slide .brand{font-size:50px;left:0;right:0;text-align:center;top:168px}
.pres-title{position:absolute;right:22px;top:298px;color:var(--white);font-weight:300;font-size:28px;text-align:right;line-height:1}
.pres-date{position:absolute;right:22px;top:330px;color:rgba(255,255,255,.8);font-weight:300;font-size:13px}
.title-band{position:absolute;left:0;right:0;bottom:0;height:72px;background:var(--navy)}
.band-main{position:absolute;left:11px;top:19px;color:var(--white);font-size:20px;font-weight:300}
.band-main b{font-weight:700}
.band-sub{position:absolute;left:11px;top:40px;color:var(--blue);font-size:13px}
.band-sub b{font-weight:500}
.band-icon{position:absolute;right:14px;top:12px;width:67px;height:51px;background:#353d4d;border:1px solid var(--navy-line)}
.band-icon svg{position:absolute;left:21px;top:13px}

/* body slides */
.slide-head{position:absolute;left:0;top:0;width:100%;height:54px;background:var(--white);border-bottom:1px solid var(--rule);text-align:center}
.slide-head h2{font-weight:300;color:var(--blue);font-size:27px;line-height:1;padding-top:6px;letter-spacing:.3px}
.slide-head p{font-size:9.5px;color:var(--grey);letter-spacing:.3px;margin-top:3px}
.slide-head p b{font-weight:700}
.slide-foot{position:absolute;left:0;bottom:0;width:100%;height:36px;background:var(--navy)}
.slide-foot .brand{font-size:14px;left:12px;top:10px;letter-spacing:1px}
.foot-label{position:absolute;left:99px;top:13px;font-size:9.5px;color:var(--white);font-weight:500}
.foot-label span{color:var(--blue);font-weight:400}
.foot-label span b{font-weight:700}
.page-no{position:absolute;right:14px;top:12px;color:var(--blue);font-size:10px}

.hero-image{position:absolute;left:38px;top:79px;width:504px;height:224px;background:linear-gradient(180deg,var(--blue) 0%,var(--blue-deep) 100%)}
.hero-image svg{position:absolute;left:198px;top:58px}
.note{position:absolute;left:38px;width:504px;padding-left:28px;font-size:8.6px;line-height:1.25;color:var(--ink);text-align:justify}
.note b{font-weight:700}
.note i{position:absolute;left:2px;top:2px;width:15px;height:15px;border-radius:50%;background:var(--blue)}

/* tables */
.table-block{position:absolute;top:74px;width:260px}
.table-title{font-size:16px;color:var(--navy);font-weight:300;height:29px;display:flex;align-items:center;gap:6px}
.table-title b{font-weight:500}
.plan{width:260px;border-collapse:collapse;font-size:6.2px;color:#777}
.plan th{height:24px;font-size:8.5px;font-weight:500;text-align:center}
.plan td{height:25.3px;padding:0 3px;border-bottom:1px solid #ececec}
.plan td.num{width:34px;text-align:center;color:var(--blue);font-size:9px}
.plan td.step{width:97px;line-height:1.1}
.plan td.who{width:70px}
.plan td.when{text-align:center}
.plan-light th{background:var(--navy);color:var(--blue)}
.plan-light td{background:var(--white)}
.plan-dark th{background:var(--blue);color:var(--white)}
.plan-dark td{background:var(--navy);color:#aab0bb;border-bottom-color:var(--navy-line)}
.table-more{height:25px;font-size:9px;text-align:center;line-height:25px}
.table-more.light{background:var(--blue);color:rgba(255,255,255,.7)}
.table-more.dark{background:var(--navy);color:var(--blue);border-top:2px solid var(--blue-deep)}

/* graphs */
.graph-title{position:absolute;top:78px;font-size:16px;color:var(--navy);font-weight:300}
.graph-title b{font-weight:500}
.graph-svg{position:absolute;left:0;top:0}
.graph-notes{position:absolute;top:310px;width:232px;font-size:7.6px;line-height:1.2;color:var(--ink)}
.graph-notes p{position:relative;padding-left:14px;margin-bottom:10px}
.graph-notes p::before{content:"";position:absolute;left:1px;top:2px;border-left:4px solid var(--blue);border-top:3px solid transparent;border-bottom:3px solid transparent}

/* closing */
.closing-slide{background:var(--navy)}
.closing-slide .brand{font-size:50px;left:0;right:0;text-align:center;top:188px}
.contact{position:absolute;left:15px;font-size:8px;line-height:1.2;color:var(--white);font-weight:500}
.contact h3{font-size:10px;color:var(--blue);font-weight:700}
.web{position:absolute;left:440px;top:410px;font-size:10px;color:var(--blue)}
.socials{position:absolute;left:522px;top:410px;display:flex;gap:8px}
.socials i{width:11px;height:11px;border-radius:50%;background:#4a5263}
</style>
</head>
<body>
<div class="canvas">

  <section class="slide col-a row-1">
    <div class="brand brand-blue" style="font-size:50px;left:0;right:0;text-align:center;top:188px">NORVELLE</div>
  </section>

  <section class="slide title-slide col-b row-1">
    <div class="brand brand-white">NORVELLE</div>
    <div class="pres-title">Presentation Title</div>
    <div class="pres-date">JAN 2014</div>
    <div class="title-band">
      <div class="band-main"><b>COMPANY</b> PRESENTATION</div>
      <div class="band-sub">to <b>Business</b>/Client</div>
      <div class="band-icon">
        <svg width="24" height="24" viewBox="0 0 24 24"><rect x="1" y="1" width="22" height="22" fill="none" stroke="#4fb0e4" stroke-width="2"/><circle cx="8" cy="8" r="2.5" fill="#4fb0e4"/><path d="M4 20 L10 12 L13 16 L16 11 L20 20Z" fill="#4fb0e4"/></svg>
      </div>
    </div>
  </section>

  <section class="slide col-a row-2">
    <header class="slide-head"><h2>IMAGE IN LANDSCAPE VIEW</h2><p>WITH COMPLETELY CUSTOMIZABLE ICONS</p></header>
    <div class="hero-image" role="img" aria-label="Landscape photograph placeholder">
      <svg width="108" height="108" viewBox="0 0 108 108" opacity=".35"><rect x="4" y="4" width="100" height="100" fill="none" stroke="#2f86bd" stroke-width="8"/><circle cx="32" cy="32" r="10" fill="#2f86bd"/><path d="M16 86 L40 52 L52 68 L70 44 L92 86Z" fill="#2f86bd"/></svg>
    </div>
    <p class="note" style="top:318px"><i></i><b>Aenean</b> ridiculus tortor quis interdum id habitant ad, natoque consectetuer nisl auctor libero quisque euismod ante inceptos malesuada ligula mattis.</p>
    <p class="note" style="top:353px"><i></i><b>Aenean</b> ridiculus tortor quis interdum id habitant ad, natoque consectetuer nisl auctor libero quisque euismod ante inceptos malesuada ligula mattis.</p>
    <footer class="slide-foot"><div class="brand brand-white">NORVELLE</div><div class="foot-label">COMPANY PRESENTATION <span>to <b>Business</b>/client</span></div><div class="page-no">3</div></footer>
  </section>

  <section class="slide col-b row-2">
    <header class="slide-head"><h2>COLOR STYLE TABLES</h2><p>CHOOSE FROM A <b>LIGHT</b> OR <b>DARK</b> THEME</p></header>
    <div class="table-block" style="left:22px">
      <div class="table-title"><svg width="18" height="14" viewBox="0 0 18 14"><rect x="1" y="1" width="16" height="12" fill="none" stroke="#4fb0e4" stroke-width="1.5"/><path d="M1 5H17M1 9H17M6 1V13M12 1V13" stroke="#4fb0e4" stroke-width="1.2"/></svg><span><b>Light</b> Theme</span></div>
      <table class="plan plan-light">
        <tr><th>Item</th><th>Step/Action</th><th>Responsible</th><th>Target Date</th></tr>
        <tr><td class="num">1</td><td class="step">Business X, Y, Z high level needs</td><td class="who">Business X, Y, Z</td><td class="when">5/24/2013</td></tr>
        <tr><td class="num">2</td><td class="step">Understand current situation and safety mana</td><td class="who">Business X, Y, Z</td><td class="when">5/31/2013</td></tr>
        <tr><td class="num">3</td><td class="step">Submit Proposal</td><td class="who">Business X, Y, Z</td><td class="when">6/3/2013</td></tr>
        <tr><td class="num">4</td><td class="step">Review Proposal</td><td class="who">Business X, Y, Z</td><td class="when">TBD</td></tr>
        <tr><td class="num">5</td><td class="step">Prepare Final Proposal &amp; Statement of Work (SOW)</td><td class="who">Business X, Y, Z</td><td class="when">TBD</td></tr>
        <tr><td class="num">6</td><td class="step">Complete and sign SOW</td><td class="who">Business X, Y, Z</td><td class="when">TBD</td></tr>
        <tr><td class="num">7</td><td class="step">Schedule project start date</td><td class="who">Business X, Y, Z</td><td class="when">TBD</td></tr>
        <tr><td class="num">8</td><td class="step">Kick-off Project</td><td class="who">Business X, Y, Z</td><td class="when">TBD</td></tr>
        <tr><td class="num">9</td><td class="step">Complete Project</td><td class="who">Business X, Y, Z</td><td class="when">TBD</td></tr>
      </table>
      <div class="table-more light">+ Additional Information</div>
    </div>
    <div class="table-block" style="left:301px">
      <div class="table-title"><svg width="18" height="14" viewBox="0 0 18 14"><rect x="1" y="1" width="16" height="12" fill="none" stroke="#4fb0e4" stroke-width="1.5"/><path d="M1 5H17M1 9H17M6 1V13M12 1V13" stroke="#4fb0e4" stroke-width="1.2"/></svg><span><b>Dark</b> Theme</span></div>
      <table class="plan plan-dark">
        <tr><th>Item</th><th>Step/Action</th><th>Responsible</th><th>Target Date</th></tr>
        <tr><td class="num">1</td><td class="step">Business X, Y, Z high level needs</td><td class="who">Business X, Y, Z</td><td class="when">5/24/2013</td></tr>
        <tr><td class="num">2</td><td class="step">Understand current situation and safety mana</td><td class="who">Business X, Y, Z</td><td class="when">5/31/2013</td></tr>
        <tr><td class="num">3</td><td class="step">Submit Proposal</td><td class="who">Business X, Y, Z</td><td class="when">6/3/2013</td></tr>
        <tr><td class="num">4</td><td class="step">Review Proposal</td><td class="who">Business X, Y, Z</td><td class="when">TBD</td></tr>
        <tr><td class="num">5</td><td class="step">Prepare Final Proposal &amp; Statement of Work (SOW)</td><td class="who">Business X, Y, Z</td><td class="when">TBD</td></tr>
        <tr><td class="num">6</td><td class="step">Complete and sign SOW</td><td class="who">Business X, Y, Z</td><td class="when">TBD</td></tr>
        <tr><td class="num">7</td><td class="step">Schedule project start date</td><td class="who">Business X, Y, Z</td><td class="when">TBD</td></tr>
        <tr><td class="num">8</td><td class="step">Kick-off Project</td><td class="who">Business X, Y, Z</td><td class="when">TBD</td></tr>
        <tr><td class="num">9</td><td class="step">Complete Project</td><td class="who">Business X, Y, Z</td><td class="when">TBD</td></tr>
      </table>
      <div class="table-more dark">+ Additional Information</div>
    </div>
    <footer class="slide-foot"><div class="brand brand-white">NORVELLE</div><div class="foot-label">COMPANY PRESENTATION <span>to <b>Business</b>/client</span></div><div class="page-no">5</div></footer>
  </section>

  <section class="slide col-a row-3">
    <header class="slide-head"><h2>COLOR STYLE GRAPHS</h2><p>CHOOSE TO USE BETWEEN <b>MAIN</b> AND <b>SECONDARY</b> COLOR THEMES</p></header>
    <div class="graph-title" style="left:28px"><b>Graph</b> Main Colors</div>
    <div class="graph-title" style="left:330px"><b>Graph</b> Secondary Colors</div>
    <svg class="graph-svg" width="582" height="400" viewBox="0 0 582 400" font-family="Roboto, Arial, sans-serif">
      <g stroke="#e3e5e8" stroke-width="1">
        <line x1="48" y1="119" x2="263" y2="119"/><line x1="48" y1="161" x2="263" y2="161"/><line x1="48" y1="202" x2="263" y2="202"/><line x1="48" y1="244" x2="263" y2="244"/>
      </g>
      <g font-size="7.5" fill="#333">
        <text x="28" y="122">100</text><text x="32" y="164">75</text><text x="32" y="205">50</text><text x="32" y="247">25</text><text x="36" y="289">0</text>
        <text x="39" y="297">2007</text><text x="111" y="297">2008</text><text x="182" y="297">2009</text><text x="252" y="297">2010</text>
      </g>
      <polygon points="48,194 120,214 191,169 240,176 263,286 48,286" fill="#3d4556"/>
      <polygon points="48,238 100,252 48,258" fill="var(--teal-soft)"/>
      <polygon points="48,258 120,241 191,198 263,127 263,286 48,286" fill="#4fb0e4"/>
      <line x1="48" y1="286" x2="263" y2="286" stroke="#777" stroke-width="1"/>
      <path d="M418 202 L462.6 118.1 A95 95 0 0 1 500.6 155.1Z" fill="var(--white)"/>
      <path d="M418 202 L368.2 282.9 A95 95 0 0 1 462.6 118.1Z" fill="#4fb0e4"/>
      <path d="M418 202 L506.8 235.7 A95 95 0 0 1 368.2 282.9Z" fill="var(--pie-purple)"/>
      <path d="M418 202 L500.6 155.1 A95 95 0 0 1 506.8 235.7Z" fill="var(--pie-pink)"/>
      <path d="M423.6 196.3 L468.2 112.4 A95 95 0 0 1 506.2 149.4Z" fill="var(--pie-green)" stroke="#fff" stroke-width="2"/>
      <g font-size="10" fill="#fff"><text x="367" y="181">50%</text><text x="466" y="153">9%</text><text x="472" y="202">14%</text><text x="428" y="266">28%</text></g>
      <g font-size="7.5" fill="#333">
        <circle cx="520" cy="257" r="3.5" fill="var(--pie-green)"/><text x="529" y="260">2007</text>
        <circle cx="520" cy="268" r="3.5" fill="var(--pie-pink)"/><text x="529" y="271">2008</text>
        <circle cx="520" cy="279" r="3.5" fill="var(--pie-purple)"/><text x="529" y="282">2009</text>
        <circle cx="520" cy="290" r="3.5" fill="#4fb0e4"/><text x="529" y="293">2010</text>
      </g>
    </svg>
    <div class="graph-notes" style="left:40px">
      <p><b>Aenean</b> ridiculus tortor quis interdum id habitant ad, natoque consectetuer nisl auctor libero quisque euismod ante inceptos malesuada ligula mattis.</p>
      <p>Varius inceptos <b>nascetur</b> mollis dui aptent ultrices. Pretium pulvinar ante lobortis convallis lectus netus vitae penatibus eros at blandit. Parturient.</p>
    </div>
    <div class="graph-notes" style="left:324px">
      <p><b>Aenean</b> ridiculus tortor quis interdum id habitant ad, natoque consectetuer nisl auctor libero quisque euismod ante inceptos malesuada ligula mattis.</p>
      <p>Varius inceptos <b>nascetur</b> mollis dui aptent ultrices. Pretium pulvinar ante lobortis convallis lectus netus vitae penatibus eros at blandit. Parturient.</p>
    </div>
    <footer class="slide-foot"><div class="brand brand-white">NORVELLE</div><div class="foot-label">COMPANY PRESENTATION <span>to <b>Business</b>/client</span></div><div class="page-no">7</div></footer>
  </section>

  <section class="slide closing-slide col-b row-3">
    <div class="brand brand-white">NORVELLE</div>
    <div class="contact" style="top:345px"><h3>Contact us:</h3>555-010-0199<br>info@norvelle.com</div>
    <div class="contact" style="top:390px"><h3>Central Office</h3>Address Line 1<br>Address Line 2</div>
    <div class="web">www.norvelle.com</div>
    <div class="socials"><i></i><i></i><i></i></div>
  </section>

</div>
</body>
</html>
```